Walk Boldly into Morning: 48 Days to a Year of Courage and Calm

This is a non-fiction, self-help book. The first edition was published a decade ago, and it needs a new design. Nothing too literal (no actual hearts on the cover) but something inspirational or perhaps something quite plain. The current cover is below for reference, but I DO NOT want something similar to that. It is outdated.

The cover must include:

1. Title: Walk Boldly into Morning
2. Subtitle: 48 Days to a Year of Courage and Calm
3. Author Name: Dean Forsythe

It should also have plenty of "white space" in other words the fonts shouldnt be so big that they take up the whole cover.

Dimensions: 9" x 6.25"

Target Market(s)

adults interested in personal development

Font styles to use
Serif
Script

Colors

Designer to choose colors to be used in the design.

Requirements
Must have
• Classic look and feel. The current design is too busy. I have included examples of the style I like below. I'm open to a singular graphic/photo but nothing more than that. Probably plain text is best.
• Please look at the samples I have included of best-selling books in the genre that I like. The cover should be modeled after these.

```html
<!DOCTYPE html>
<html lang="en">
<head>
<meta charset="utf-8">
<title>Walk Boldly into Morning — Cover</title>
<link rel="stylesheet" href="https://fonts.googleapis.com/css2?family=Cormorant+Garamond:wght@500;600&family=Great+Vibes&family=Playfair+Display:wght@600;700&display=swap">
<style>
  :root {
    --page-bg: #ffffff;
    --cover-paper: #f3f1ed;
    --ink: #141414;
    --ember: #e2532f;
    --ember-deep: #c9421f;
    --band-text: #ffffff;
  }
  html, body {
    margin: 0;
    padding: 0;
    width: 1200px;
    height: 1103px;
    overflow: hidden;
    background: var(--page-bg);
  }
  .book-cover {
    position: absolute;
    left: 250px;
    top: 26px;
    width: 700px;
    height: 1050px;
    display: block;
  }
  .cover-paper { fill: var(--cover-paper); }
  .title-line {
    font-family: "Playfair Display", "Times New Roman", serif;
    font-weight: 700;
    fill: var(--ink);
    letter-spacing: 1px;
  }
  .title-connector {
    font-family: "Great Vibes", "Brush Script MT", cursive;
    fill: var(--ink);
  }
  .title-accent {
    font-family: "Playfair Display", "Times New Roman", serif;
    font-weight: 700;
    fill: var(--ember);
    letter-spacing: 4px;
  }
  .subtitle-band { fill: var(--ember); }
  .subtitle-band-edge { fill: var(--ember-deep); opacity: 0.3; }
  .subtitle {
    font-family: "Cormorant Garamond", "Times New Roman", serif;
    font-weight: 500;
    fill: var(--band-text);
  }
  .author {
    font-family: "Playfair Display", "Times New Roman", serif;
    font-weight: 600;
    fill: var(--ink);
    letter-spacing: 6px;
  }
</style>
</head>
<body>
<svg class="book-cover" viewBox="0 0 700 1050" xmlns="http://www.w3.org/2000/svg" aria-label="Book cover: Walk Boldly into Morning by Dean Forsythe">
  <rect class="cover-paper" x="0" y="0" width="700" height="1050"/>

  <g class="title">
    <text class="title-line" x="350" y="250" font-size="82" text-anchor="middle">Walk Boldly</text>
    <text class="title-connector" x="350" y="360" font-size="96" text-anchor="middle">into</text>
    <text class="title-accent" x="350" y="520" font-size="92" text-anchor="middle">MORNING</text>
  </g>

  <g class="subtitle-block">
    <polygon class="subtitle-band-edge"
      points="63,668 110,662 170,666 240,660 310,664 380,658 450,662 520,657 590,660 650,654 700,652 700,672 63,684"/>
    <polygon class="subtitle-band"
      points="63,670 105,665 160,668 230,662 300,667 370,661 440,665 510,660 580,663 640,657 700,655
              700,806 660,808 610,812 560,809 510,814 455,810 400,816 340,812 280,818 220,814 160,817 110,813 66,815 60,740"/>
    <text class="subtitle" x="370" y="728" font-size="44" text-anchor="middle">48 Days to a Year of</text>
    <text class="subtitle" x="370" y="782" font-size="44" text-anchor="middle">Courage and Calm</text>
  </g>

  <text class="author" x="350" y="975" font-size="44" text-anchor="middle">DEAN FORSYTHE</text>
</svg>
</body>
</html>
```